Digital One Pager for Consulting Practice

I would like the essence of the content in my ppt consolidated into a one-pager. The one-pager will mainly be sent via email as a pdf and intended to excite and invite new clients and establish the credibility of my boutique high-end consulting firm. Infographics and symbols would be a plus. The target client should view the firm as providing premeir service. The client is getting a thought partner.

Target Market(s)

Large Medical Device Manufacturer Executives, Early-Stage Medical Device Manufacturer Executives, Partners at VC Firms

Industry/Entity Type

Medical Equipment

Colors
0355a3
f37122

Requirements
Must have
• Please match the color scheme in ppt. Please use the existing logo. I am very open to better graphics on the process. My photo does not need to be on the digital flyer. Hyper link to the website and email is needed.
Nice to have
• Infographics

```html
<!DOCTYPE html>
<html lang="en">
<head>
<meta charset="utf-8">
<title>Halden Ventures – One Pager</title>
<link href="https://fonts.googleapis.com/css2?family=Tinos:wght@400;700&family=Nunito+Sans:wght@400;600;700&display=swap" rel="stylesheet">
<style>
:root{
  --navy:#0c1a3d;
  --blue:#0355a3;
  --band:#1160b5;
  --orange:#f37122;
  --ink:#1f2a44;
  --muted:#6b7280;
  --stage:#d9d9d9;
}
*{margin:0;padding:0;box-sizing:border-box}
html,body{width:1200px;height:1200px;overflow:hidden;background:var(--stage)}
body{font-family:"Nunito Sans",sans-serif;color:var(--ink)}
.flyer{position:absolute;left:191px;top:23px;width:764px;height:1078px;background:#fff;transform:scale(1.07);transform-origin:0 0;overflow:hidden}
.abs{position:absolute}
.serif{font-family:"Tinos",serif}
a{color:inherit;text-decoration:none}

.header{left:0;top:0;width:764px;height:196px;background:var(--navy);color:#fff;text-align:center}
.brand{left:0;top:36px;width:764px;display:flex;justify-content:center;align-items:center;gap:10px}
.brand-mark{width:14px;height:14px;background:var(--orange)}
.brand-name{font-size:30px;font-weight:700;letter-spacing:4px;color:#fff;line-height:1}
.title{left:0;top:96px;width:764px;font-size:38px;letter-spacing:.5px}
.tagline{left:0;top:147px;width:764px;font-size:16px}

.intro{left:0;top:196px;width:764px;height:194px;background:linear-gradient(#fff 80%,#eef0f3)}
.portrait{left:129px;top:218px;width:104px;height:104px;border-radius:50%;background:radial-gradient(circle at 50% 40%,#6a5446,#2b2724)}
.portrait-cap{left:80px;top:325px;width:200px;text-align:center}
.portrait-cap .lead{color:var(--orange);font-size:14px}
.portrait-cap .sub{font-size:10.5px}

h2{font-family:"Tinos",serif;font-weight:400;color:var(--blue);font-size:22px;line-height:1}
.rule{height:2px;background:var(--orange)}
ul{list-style:none}
li{position:relative;padding-left:10px;font-size:12px;line-height:15px}
li::before{content:"•";position:absolute;left:0;color:var(--orange)}
.blue-dot li::before{color:var(--blue)}

.svc-title{color:var(--orange);font-size:16px;font-weight:600;line-height:1}
.svc-list{font-size:12px}
.svc-row{display:flex;gap:20px}

.step-label{color:var(--blue);font-size:12.5px;font-weight:600;text-align:center;line-height:14px;width:110px}

.partners-band{left:0;top:920px;width:764px;height:36px;background:var(--band);color:#fff;text-align:center;font-size:25px;line-height:38px}
.partners{left:40px;top:978px;width:690px;display:flex;justify-content:space-between;align-items:center}
.partner{display:flex;align-items:center;gap:5px;font-size:12px;font-weight:700;color:var(--blue)}
.partner i{display:block;width:10px;height:10px;background:var(--blue)}
.partner.gray{color:#6b7280;letter-spacing:2px;font-weight:400}

.footer{left:0;top:1042px;width:764px;height:36px;background:var(--orange);color:#fff;display:flex;justify-content:center;align-items:center;gap:18px;font-size:17.5px;font-weight:600}
.footer span{display:flex;align-items:center;gap:6px}
</style>
</head>
<body>
<main class="flyer">
  <header class="abs header">
    <div class="abs brand"><span class="brand-mark"></span><span class="brand-name">HALDEN VENTURES</span></div>
    <div class="abs title serif">HALDEN VENTURES VALUE</div>
    <div class="abs tagline serif">Extensive Experience |&nbsp; Efficient Process |&nbsp;Valued Network</div>
  </header>

  <section class="abs intro"></section>
  <div class="abs portrait" role="img" aria-label="Portrait photo of the firm's founder"></div>
  <div class="abs portrait-cap"><div class="lead">Over a decade @FDA</div><div class="sub">(Former Deputy Division Director)</div></div>

  <section class="abs" style="left:271px;top:221px;width:440px">
    <h2>EXPERIENCE</h2>
    <ul style="margin-top:12px">
      <li>Expertise: Cardiovascular, Ophthalmology, General Hospital, Infection Control, Dental, Anesthesia, Respiratory</li>
      <li style="margin-top:14px">Vice President Regulatory Affairs / Quality Assurance @Corvane (Fortune 150 Company)</li>
    </ul>
    <ul style="margin-left:16px">
      <li>Initiated&nbsp; reorganization of department</li>
      <li>Led major compliance effort</li>
      <li>Successful FDA inspection (no observations)</li>
    </ul>
  </section>

  <!-- Differentiators -->
  <section class="abs" style="left:0;top:410px;width:330px">
    <h2 class="abs" style="left:61px;top:0">DIFFERENTIATORS</h2>
    <div class="abs rule" style="left:95px;top:25px;width:136px"></div>
    <svg class="abs" style="left:0;top:0" width="330" height="220" viewBox="0 0 330 220" fill="none" stroke="#0355a3" stroke-width="2.2">
      <circle cx="158" cy="47" r="5" stroke="#f37122"/>
      <path d="M158 52v10M158 62l-12 14M158 62l12 14M146 76l-9 12M146 76l5 12M170 76l-5 12M170 76l9 12"/>
      <circle cx="137" cy="92" r="4"/><circle cx="151" cy="92" r="4"/><circle cx="165" cy="92" r="4"/><circle cx="179" cy="92" r="4"/>
      <path d="M158 118v12M65 130h183M65 130v14M158 130v14M248 130v14"/>
      <circle cx="66" cy="162" r="14"/><path d="M66 154l3 6 6 1-5 4 1 6-5-3-5 3 1-6-5-4 6-1z" fill="#0355a3" stroke="none"/>
      <path d="M56 174l-4 16 14-7 14 7-4-16M48 156a8 8 0 0 0 4 12M84 156a8 8 0 0 1-4 12"/>
      <circle cx="158" cy="163" r="5"/><circle cx="142" cy="148" r="3.5"/><circle cx="174" cy="148" r="3.5"/><circle cx="142" cy="178" r="3.5"/><circle cx="174" cy="178" r="3.5"/>
      <path d="M145 151l9 8M171 151l-9 8M145 175l9-8M171 175l-9-8"/>
      <rect x="224" y="148" width="20" height="10"/><rect x="252" y="150" width="10" height="6"/><rect x="228" y="166" width="10" height="6"/><rect x="244" y="164" width="20" height="10"/>
      <path d="M234 158v8M262 156v8M224 178h40" stroke-width="1.8"/>
    </svg>
    <div class="abs" style="left:119px;top:105px;color:var(--orange);font-size:15px">LEVERAGE</div>
    <div class="abs" style="left:31px;top:195px;color:#6b7280;font-size:13px">Experience</div>
    <div class="abs" style="left:131px;top:195px;color:#6b7280;font-size:13px">Network</div>
    <div class="abs" style="left:222px;top:195px;color:#6b7280;font-size:13px">Process</div>
  </section>

  <!-- Services -->
  <section class="abs" style="left:368px;top:410px;width:380px">
    <h2>SERVICES</h2>
    <div class="rule" style="width:64px;margin-top:3px"></div>
    <svg class="abs" style="left:-2px;top:46px" width="44" height="200" viewBox="0 0 44 200" fill="none" stroke="#0355a3" stroke-width="2">
      <path d="M8 14a10 10 0 0 1 14-8 10 10 0 0 1 14 8 8 8 0 0 1 0 14 9 9 0 0 1-14 6 9 9 0 0 1-14-6 8 8 0 0 1 0-14z"/>
      <path d="M22 6v28M14 18h16M14 26h16"/><circle cx="14" cy="18" r="2"/><circle cx="30" cy="26" r="2"/>
      <path d="M12 66l5 4 5-6 5 6 5-4-2 8H14z" fill="#0355a3"/><circle cx="22" cy="82" r="6" fill="#0355a3"/>
      <path d="M10 104v-8a12 12 0 0 1 24 0v8z" fill="#0355a3"/>
      <rect x="4" y="122" width="24" height="16" rx="2"/><path d="M10 138l-4 6v-6"/><rect x="16" y="130" width="24" height="16" rx="2"/><path d="M24 138h2M28 138h2M32 138h2"/>
      <rect x="10" y="160" width="24" height="14"/><path d="M15 170v-4M20 170v-6M25 170v-3M30 170v-5"/>
      <circle cx="12" cy="182" r="3"/><circle cx="22" cy="182" r="3"/><circle cx="32" cy="182" r="3"/>
      <path d="M6 194a6 6 0 0 1 12 0zM16 194a6 6 0 0 1 12 0zM26 194a6 6 0 0 1 12 0z"/>
    </svg>
    <div class="abs" style="left:59px;top:47px">
      <div class="svc-title">REGULATORY STRATEGY</div>
      <ul class="blue-dot svc-list"><li>RAQA Organizational Structure</li><li>Regulatory Pathway</li></ul>
    </div>
    <div class="abs" style="left:59px;top:101px">
      <div class="svc-title">INTERIM EXECUTIVE LEADERSHIP</div>
      <ul class="blue-dot svc-list"><li>Compliance Remediation</li><li>Accelerated Product Registration</li></ul>
    </div>
    <div class="abs" style="left:59px;top:158px">
      <div class="svc-title">FDA COMMUNICATIONS</div>
      <ul class="blue-dot svc-list svc-row"><li>Deficiency Response</li><li>Application Review</li></ul>
    </div>
    <div class="abs" style="left:59px;top:200px">
      <div class="svc-title">TRAINING</div>
      <ul class="blue-dot svc-list svc-row"><li>FDA Communication</li><li>MDR Reporting</li></ul>
    </div>
  </section>

  <!-- Experience to provide -->
  <section class="abs" style="left:46px;top:668px;width:215px">
    <h2 style="line-height:20px">EXPERIENCE<br>TO PROVIDE...</h2>
    <div class="rule" style="width:72px;margin-top:3px"></div>
    <div style="color:var(--orange);font-size:13px;margin-top:7px">Executive Application Review</div>
    <ul class="blue-dot" style="font-size:12px">
      <li>Examples include: Presubmission, IDE, 510(k) , 513(g), PMA, Refuse to Accept, Hold letter</li>
      <li>Troubleshooting</li>
    </ul>
    <div style="color:var(--orange);font-size:13px;line-height:14px;margin-top:6px">Strategic Advice &amp; Diligence to Investors</div>
    <ul class="blue-dot" style="margin-top:3px">
      <li>Validate &amp; Verify Founder Milestones</li>
      <li>Diligence portfolio company Regulatory &amp; Quality systems</li>
    </ul>
  </section>

  <!-- Efficient process -->
  <section class="abs" style="left:260px;top:678px;width:490px;height:240px">
    <h2 class="abs" style="left:130px;top:0">EFFICIENT PROCESS</h2>
    <div class="abs rule" style="left:205px;top:27px;width:72px"></div>
    <svg class="abs" style="left:0;top:40px" width="490" height="120" viewBox="0 0 490 120">
      <defs>
        <linearGradient id="bo" x1="0" x2="1"><stop offset="0" stop-color="#0355a3"/><stop offset="1" stop-color="#f37122"/></linearGradient>
        <linearGradient id="ob" x1="0" x2="1"><stop offset="0" stop-color="#f37122"/><stop offset="1" stop-color="#0355a3"/></linearGradient>
      </defs>
      <path d="M100 80L140 30 150 44 110 92z" fill="url(#bo)"/>
      <path d="M220 80L260 30 270 44 230 92z" fill="url(#ob)"/>
      <path d="M340 80L380 30 390 44 350 92z" fill="url(#bo)"/>
      <g>
        <circle cx="66" cy="60" r="50" fill="#0355a3"/><circle cx="66" cy="60" r="32" fill="#e8f0fa"/>
        <circle cx="185" cy="60" r="50" fill="#f37122"/><circle cx="185" cy="60" r="32" fill="#fdeee4"/>
        <circle cx="305" cy="60" r="50" fill="#0355a3"/><circle cx="305" cy="60" r="32" fill="#e8f0fa"/>
        <circle cx="424" cy="60" r="50" fill="#f37122"/><circle cx="424" cy="60" r="32" fill="#fdeee4"/>
      </g>
      <path d="M56 48c-4 4 0 16 10 24 6 4 10 4 12 1l-5-5-4 3c-4-2-8-7-9-10l3-4-5-6z" fill="#f37122"/>
      <path d="M72 46a10 10 0 0 1 8 8M74 40a16 16 0 0 1 12 12" stroke="#f37122" stroke-width="2" fill="none"/>
      <g fill="none" stroke="#0355a3" stroke-width="2"><rect x="172" y="42" width="24" height="34" rx="2"/><path d="M177 52l2 2 4-4M186 52h6M177 60l2 2 4-4M186 60h6M177 68l2 2 4-4M186 68h6M200 46v28l-3 5-3-5V46z"/></g>
      <circle cx="305" cy="58" r="15" fill="none" stroke="#f37122" stroke-width="2.4"/><path d="M300 72l-3 6 7-4" fill="#f37122"/>
      <path d="M305 49v11" stroke="#f37122" stroke-width="3"/><circle cx="305" cy="65" r="1.8" fill="#f37122"/>
      <g fill="none" stroke="#0355a3" stroke-width="2"><rect x="416" y="40" width="18" height="16"/><path d="M422 40v6l3-2 3 2v-6M408 72l8-6h14l-2 5h-8M408 76l6 0 14 0 14-12 2 4-14 14h-22"/></g>
    </svg>
    <div class="abs step-label" style="left:11px;top:168px">EXPLORATORY<br>CALL</div>
    <div class="abs step-label" style="left:130px;top:168px">REGULATORY<br>LANDSCAPE</div>
    <div class="abs step-label" style="left:250px;top:168px">PROBLEM<br>STATEMENT</div>
    <div class="abs step-label" style="left:369px;top:168px">REVIEW &amp;<br>ALIGN ON<br>DELIVERABLES</div>
  </section>

  <div class="abs partners-band serif">VALUED PARTNER NETWORK</div>
  <div class="abs partners">
    <span class="partner"><i></i>Westfield Tech Group</span>
    <span class="partner">Harbor Angels</span>
    <span class="partner">MedBridge Labs</span>
    <span class="partner">Stafflink</span>
    <span class="partner">Pryce Law</span>
    <span class="partner gray">MERIDIA GROUP</span>
  </div>

  <footer class="abs footer">
    <span><svg width="15" height="15" viewBox="0 0 16 16"><circle cx="8" cy="8" r="7" fill="#fff"/></svg><a href="https://www.haldenventures.com">www.haldenventures.com</a></span>
    <span><svg width="16" height="16" viewBox="0 0 16 16"><path d="M3 2l3 0 1 4-2 1c1 2 3 4 5 5l1-2 4 1v3c0 1-1 1-2 1C7 15 1 9 1 4c0-1 1-2 2-2z" fill="#fff"/></svg>202.555.0147</span>
    <span><svg width="16" height="12" viewBox="0 0 16 12"><rect width="16" height="12" fill="#fff"/><path d="M0 0l8 6 8-6" stroke="#f37122" stroke-width="1.5" fill="none"/></svg><a href="mailto:info@haldenventures.com">info@haldenventures.com</a></span>
  </footer>
</main>
</body>
</html>
```